'Cradle Ahead' promotional brochure

We have designed a 6 week program to educate impending first-time parents about the things they need to know to survive the first 6 months. Sessions delivered by general practitioner/family doctor, dietician, physiotherapist, speech pathologist and psychologist. Our promotional blurb is: 'A comprehensive education program for first-time parents-to-be, delivered over 6 weeks by health professionals in your community, about everything you need to know to look after your baby (and yourself!) in the first 6 months'. I now want to put together a promotional brochure to be distributed to those couples who express an interest which will provide further details of what will be delivered in the course.
Updates
In terms of layout, I envisaged a double sided A4 size, foldable into 3 sections, but very happy to be guided on this.
Target Market(s)
To appeal to a young, well educated demographic. First time parents couples.
Industry/Entity Type
Medical
Font styles to use
Other font styles liked:
- Playfair Display
Requirements
Must have
- Playfair display font to be consistent with our logo (attached). Logo also included please. Some consistency with colours of logo please.
Nice to have
- I am a doctor, and have no creative genes! But prefer a clean and professional appearance overall. Not too cluttered in overall appearance.
Should not have
- No cheesy pictures of babies.

```html
<!DOCTYPE html>
<html lang="en">
<head>
<meta charset="utf-8">
<title>Cradle Ahead – Program Sessions</title>
<link rel="stylesheet" href="https://fonts.googleapis.com/css2?family=Arimo:wght@400;700&display=swap">
<style>
  :root {
    --green: #6cbf46;
    --green-pale: #e0f0d7;
    --grey-panel: #e5e5e5;
    --grey-panel-dark: #e1e1e1;
    --heading-grey: #7a7a7a;
    --text: #2b2b2b;
    --white: #ffffff;
  }
  * { box-sizing: border-box; margin: 0; padding: 0; }
  html, body { width: 1200px; height: 848px; overflow: hidden; background: var(--white); }
  body { font-family: "Arimo", Arial, sans-serif; color: var(--text); }
  .spread { position: relative; width: 1200px; height: 848px; }
  .week-title {
    position: absolute; top: 40px;
    font-size: 24px; font-weight: 700; color: var(--heading-grey);
  }
  .week-title--accent { color: var(--green); }
  .panel { position: absolute; }
  .panel--week1 { left: 0; top: 96px; width: 400px; height: 236px; background: var(--grey-panel); padding: 24px 26px; }
  .panel--week2 { left: 400px; top: 96px; width: 400px; height: 308px; background: var(--green); padding: 22px 26px; }
  .panel--week4 { left: 800px; top: 96px; width: 400px; height: 308px; background: var(--green-pale); padding: 22px 26px; }
  .panel--week3 { left: 400px; top: 412px; width: 498px; height: 436px; background: var(--grey-panel-dark); padding: 28px 26px; }
  .intro, .session { font-size: 15.5px; line-height: 19.2px; }
  .intro { margin-bottom: 2px; }
  .presenter { color: var(--green); font-weight: 700; }
  .topics { list-style: none; }
  .topics li { position: relative; padding-left: 16px; font-size: 15.5px; line-height: 23px; }
  .panel--week4 .topics li { line-height: 22.6px; }
  .topics li::before {
    content: ""; position: absolute; left: 2px; top: 7px;
    border-left: 7px solid var(--green);
    border-top: 5px solid transparent; border-bottom: 5px solid transparent;
  }
  .session { margin-bottom: 19px; }
  .session-label { font-size: 17.5px; font-weight: 700; color: var(--green); }
  .panel--week2 .session-label { color: #2c3a22; }
  .panel--week2 .session { color: var(--white); }
  .week3-title { font-size: 24px; font-weight: 700; color: var(--white); margin-bottom: 22px; }
  .panel--week3 .session { margin-bottom: 20px; }
  .photo { position: absolute; }
  .photo--vaccine { left: 0; top: 338px; width: 400px; height: 214px; background: linear-gradient(135deg, #f2f4f7 0%, #c9d9ee 45%, #3f78c4 70%, #e9edf2 100%); }
  .photo--feeding { left: 0; top: 558px; width: 400px; height: 290px; background: linear-gradient(160deg, #f0d6c4 0%, #dcae92 50%, #c48a6c 100%); }
  .photo--newborn { left: 904px; top: 412px; width: 296px; height: 176px; background: linear-gradient(135deg, #f1f1f1 0%, #f0cbb8 55%, #e7e7e7 100%); }
  .photo--cuddle { left: 904px; top: 594px; width: 296px; height: 254px; background: linear-gradient(150deg, #f4f4f4 0%, #e9c9b3 55%, #b48263 100%); }
</style>
</head>
<body>
<main class="spread">
  <h2 class="week-title" style="left:56px">Week 1</h2>
  <h2 class="week-title week-title--accent" style="left:456px">Week 2</h2>
  <h2 class="week-title" style="left:856px">Week 4</h2>

  <section class="panel panel--week1">
    <p class="intro">GP <span class="presenter">Dr Helena Marsh</span> will share information for Mum’s own health after delivery.<br>Topics include:</p>
    <ul class="topics">
      <li>Vaccinations in pregnancy</li>
      <li>Bleeding, bladder and bowel after delivery</li>
      <li>Breastfeeding, engorgement and mastitis</li>
      <li>Bottle feeding</li>
      <li>Post-natal anxiety &amp; depression</li>
      <li>Intimacy and contraception</li>
    </ul>
  </section>

  <section class="panel panel--week2">
    <p class="session"><span class="session-label">Session 1</span> – Clinical Psychologist Dr Maren Castell will discuss changes in relationships as couples becomes parents, gender roles in parenting and post-natal depression.</p>
    <p class="session"><span class="session-label">Session 2</span> – Physiotherapist Tessa Rowland will present advice for Mums regarding exercise during and after pregnancy, looking after the pelvic floor during and after pregnancy, and abdominal muscle separation management. She will also provide advice for promoting babies’ neck strength and minimising the risk of flat spots on the head and encouraging gross motor skills in the first 6 months.</p>
  </section>

  <section class="panel panel--week4">
    <p class="intro">GP <span class="presenter">Dr Helena Marsh</span> will share advice about your babies’ health in the first 6 months, including:</p>
    <ul class="topics">
      <li>Skin of newborns</li>
      <li>Sleeping</li>
      <li>Crying</li>
      <li>Immunisations</li>
      <li>Fever and infections</li>
      <li>Diarrhoea and constipation</li>
      <li>Teething</li>
      <li>Understanding a baby’s signals</li>
    </ul>
  </section>

  <section class="panel panel--week3">
    <h2 class="week3-title">Week 3</h2>
    <p class="session"><span class="session-label">Session 1</span> – Dietician Nora Whitfield provides advice for Mums regarding healthy eating during pregnancy and lactation, normal weight gain during pregnancy and realistic weight loss after. She will also discuss the evidence regarding breastfeeding VS bottle-feeding, normal infant weight gain and introducing solids (including those with potential for allergy).</p>
    <p class="session"><span class="session-label">Session 2</span> – Paediatric Speech Pathologist Claire Benton will share information about latching and breast-feeding troubles &amp; tongue tie, advice about dummies and finger-sucking, introducing solids &amp; feeding (including ‘pouch’ food), encouraging language development and current evidence about electronic devices impacting language development.</p>
  </section>

  <div class="photo photo--vaccine" role="img" aria-label="Photo: gloved hands preparing a vaccine syringe"></div>
  <div class="photo photo--feeding" role="img" aria-label="Photo: close-up of a baby breastfeeding, holding a parent's finger"></div>
  <div class="photo photo--newborn" role="img" aria-label="Photo: a crying newborn lying on a white blanket"></div>
  <div class="photo photo--cuddle" role="img" aria-label="Photo: a mother cuddling her newborn baby"></div>
</main>
</body>
</html>
```